Refresh of The Marston Collective business card

Update business card design using existing primary logo. Names, numbers, etc. are too hard to read on current design.

Target Market(s)

We are a CPA firm.

Industry/Entity Type

Accountant

Contact Information for Business Card

update current card

Colors
0355a3
3176b5
85acd3
0792cd

Requirements
Must have
• Easier to read phone numbers and names
• Use existing logo
Nice to have
• We love our color scheme and current TMC logo. But the names and phone numbers are too small and card just look old and stale.

```html
<!DOCTYPE html>
<html lang="en">
<head>
<meta charset="utf-8">
<title>The Marston Collective — Business Card</title>
<link rel="stylesheet" href="https://fonts.googleapis.com/css2?family=Michroma&display=swap">
<style>
  :root {
    --bg-deep: #0b0c0e;
    --bg-mid: #1f2125;
    --bg-lift: #34373c;
    --stripe: rgba(255,255,255,0.035);
    --blue-primary: #0355a3;
    --blue-bright: #1b3fc4;
    --blue-soft: #85acd3;
    --text-light: #f2f2f2;
    --mark-ring: rgba(150,160,175,0.14);
    --mark-fill: rgba(120,130,145,0.05);
  }
  * { margin: 0; padding: 0; box-sizing: border-box; }
  html, body { width: 1200px; height: 686px; overflow: hidden; background: var(--bg-deep); }
  .card {
    position: relative;
    width: 1200px; height: 686px;
    overflow: hidden;
    font-family: "Michroma", sans-serif;
    color: var(--text-light);
    background:
      repeating-linear-gradient(90deg, var(--stripe) 0 2px, transparent 2px 6px),
      radial-gradient(ellipse 75% 65% at 50% 30%, var(--bg-lift) 0%, var(--bg-mid) 45%, var(--bg-deep) 100%);
  }
  .brand-mark {
    position: absolute;
    left: 891px; top: 360px;
    width: 412px; height: 412px;
    border-radius: 50%;
    border: 6px solid var(--mark-ring);
    background: var(--mark-fill);
  }
  .holder-name {
    position: absolute;
    top: 142px; left: 0; width: 100%;
    text-align: center;
    font-size: 32px;
    font-weight: 400;
    letter-spacing: 1.5px;
    white-space: nowrap;
  }
  .holder-name .given { color: var(--blue-bright); }
  .holder-name .title { color: var(--blue-bright); font-style: italic; }
  .name-rule {
    position: absolute;
    top: 198px; left: 274px;
    width: 652px; height: 3px;
    background: linear-gradient(90deg, transparent, rgba(255,255,255,0.9) 50%, transparent);
  }
  .address {
    position: absolute;
    top: 256px; left: 0; width: 100%;
    text-align: center;
    font-size: 25px;
    line-height: 37px;
    letter-spacing: 2px;
    white-space: nowrap;
  }
  .phones {
    position: absolute;
    top: 362px; left: 440px;
    list-style: none;
  }
  .phones li {
    display: flex; align-items: center;
    height: 36px;
    font-size: 26px;
    letter-spacing: 1.5px;
  }
  .phones svg, .email svg { flex: none; margin-right: 14px; }
  .email {
    position: absolute;
    top: 576px; left: 284px;
    display: flex; align-items: center;
    font-size: 26px;
    letter-spacing: 0.5px;
    white-space: nowrap;
  }
  .email .domain { color: var(--blue-bright); }
  .icon-stroke { fill: none; stroke: var(--blue-bright); stroke-width: 2; }
  .icon-fill { fill: var(--blue-bright); }
</style>
</head>
<body>
<div class="card">
  <div class="brand-mark" role="img" aria-label="Faint The Marston Collective brand mark"></div>

  <h1 class="holder-name"><span class="given">DANIEL R.</span> MARSTON, <span class="title">CPA</span></h1>
  <div class="name-rule"></div>

  <p class="address">318 E. LINDEN AVE. SUITE 104<br>WINTER PARK, FLORIDA 32789</p>

  <ul class="phones">
    <li>
      <svg width="24" height="24" viewBox="0 0 24 24" aria-label="Office">
        <circle class="icon-stroke" cx="12" cy="12" r="10"/>
        <path class="icon-fill" d="M8 6.5c.6-.4 1.3-.3 1.6.3l1 1.8c.3.5.1 1-.3 1.3l-.7.5c.5 1.4 1.6 2.6 3 3.2l.5-.7c.3-.4.9-.5 1.3-.3l1.8 1c.6.3.7 1 .3 1.6l-.8 1c-.7.8-2 .9-3.2.3-2.6-1.3-4.5-3.3-5.6-5.8-.5-1.200-.3-2.5.5-3.2z"/>
      </svg>
      555.210.4381
    </li>
    <li>
      <svg width="24" height="24" viewBox="0 0 24 24" aria-label="Fax">
        <path class="icon-fill" d="M3 9c0-2 4-3.5 9-3.5S21 7 21 9v1.5h-4.5V9h-9v1.5H3z"/>
        <path class="icon-fill" d="M6 11.5h12l2 8H4z"/>
        <circle cx="12" cy="15.5" r="2" fill="#111"/>
      </svg>
      555.210.4390
    </li>
    <li>
      <svg width="24" height="24" viewBox="0 0 24 24" aria-label="Mobile">
        <rect class="icon-stroke" x="8" y="3" width="8" height="18" rx="1.5"/>
        <rect class="icon-fill" x="10" y="17" width="4" height="2"/>
      </svg>
      555.317.2046
    </li>
  </ul>

  <div class="email">
    <svg width="26" height="26" viewBox="0 0 24 24" aria-label="Email">
      <path class="icon-stroke" d="M3 10l9-7 9 7v11H3z"/>
      <path class="icon-stroke" d="M3 10l9 6 9-6"/>
    </svg>
    <span>dan@<span class="domain">themarstoncollective.</span>com</span>
  </div>
</div>
</body>
</html>
```